HIDE WARDEN

Labels for Men's Skin Care. Organic, target 25-35 The label will be 2x3.5 on a 4oz amber bottle. 3 labels with the information shown on the uploaded sample.
Our product is a e-commerce built to help my 24 year old twin sons have a business of their own. Although it will be sold online they will also do foot work and sell to barbers at barber shops using as a mist on customers after shaving. So we want something that will attract male customers and will look good in a modern Barbershop. This is there shot and packaging is very very important. So if you could help us out with a great label we would be working with you in the future for package design. Our line will have several mens Organic natural skin care cleanser, mask toners and moisturizers..Thank you for your help. We also hope to put our products in beauty supply shops. So it needs to stand out as a mans product but still be traditional male product. Oh be creative mind that you are and remember we are trying to build a brand that attracts 25-35 male. Thank you

Hello, I just wanted to let you know that I am up working very late.

for anyone on the other side of the world up and working. I sleep about
3 hours.. So I'll be up for a few more hours and then up again around 5am my time

Good morning... I just wanted to say I will need three labels.. The words on all three are not that different and will fit pretty much the same on all three. So if you could work with one showing how the colors might be a little different on the other two you can do that with just the one label Just to make it easier on you if you like.. we can fix the other two once I find the right label,  Thank you it is 3am here.. still working.. I love it.

Target Market(s)

MALE 25-35

Industry/Entity Type

E-Commerce

Requirements
Must have
• final design must be fitted to the dieline uploaded.

```html
<!DOCTYPE html>
<html lang="en">
<head>
<meta charset="utf-8">
<title>Hide Warden — Label Set</title>
<link rel="stylesheet" href="https://fonts.googleapis.com/css2?family=Cinzel:wght@500&family=Crimson+Text:wght@400;600&family=Oswald:wght@500&display=swap">
<style>
  :root {
    --page: #ffffff;
    --label-ground: #2a1a1f;
    --label-ground-deep: #1f1216;
    --gold: #c9a24a;
    --gold-soft: #a8843a;
    --cream: #efe0c2;
    --leaf-tone: #4a2a1c;
    --size-band: #3a2521;
  }
  * { box-sizing: border-box; margin: 0; padding: 0; }
  html, body {
    width: 1200px;
    height: 1000px;
    overflow: hidden;
    background: var(--page);
  }
  .label-set {
    position: relative;
    width: 1200px;
    height: 1000px;
    display: flex;
    justify-content: center;
    align-items: center;
    gap: 60px;
  }
  .label {
    position: relative;
    width: 320px;
    height: 560px;
    background: var(--label-ground);
    border: 3px solid var(--gold);
    padding: 7px;
  }
  .label-inner {
    position: relative;
    width: 100%;
    height: 100%;
    border: 1.5px solid var(--gold-soft);
    display: flex;
    flex-direction: column;
    align-items: center;
    text-align: center;
    overflow: hidden;
  }
  .leaf-field {
    position: absolute;
    left: 0; right: 0; bottom: 0;
    height: 58%;
    background: radial-gradient(ellipse at 60% 70%, var(--leaf-tone) 0%, rgba(74,42,28,0.55) 45%, rgba(42,26,31,0) 80%);
  }
  .brand-mark {
    position: relative;
    margin-top: 30px;
    width: 44px;
    height: 44px;
    border-radius: 50%;
    background: var(--gold);
  }
  .flourish {
    position: relative;
    width: 180px;
    height: 4px;
    background: var(--gold-soft);
    border-radius: 2px;
  }
  .flourish-top { margin-top: 16px; }
  .brand-name {
    position: relative;
    margin-top: 10px;
    font-family: "Cinzel", serif;
    font-weight: 500;
    font-size: 31px;
    letter-spacing: 0.5px;
    color: var(--gold);
    line-height: 1;
  }
  .flourish-bottom { margin-top: 10px; }
  .claim {
    position: relative;
    margin-top: 34px;
    font-family: "Crimson Text", serif;
    font-size: 22px;
    line-height: 1.22;
    color: var(--cream);
  }
  .product-name {
    position: relative;
    margin-top: 30px;
    font-family: "Oswald", sans-serif;
    font-weight: 500;
    font-size: 24px;
    letter-spacing: 0.2px;
    color: var(--gold);
    text-transform: uppercase;
  }
  .spacer { flex: 1; }
  .scent {
    position: relative;
    font-family: "Crimson Text", serif;
    font-size: 17px;
    color: var(--cream);
    padding: 1px 10px;
    background: rgba(58,37,33,0.7);
  }
  .volume {
    position: relative;
    margin: 4px 0 22px;
    font-family: "Crimson Text", serif;
    font-size: 22px;
    color: var(--cream);
    padding: 0 12px;
    background: var(--size-band);
  }
</style>
</head>
<body>
<main class="label-set">

  <article class="label">
    <div class="label-inner">
      <div class="leaf-field" role="img" aria-label="Dark botanical leaf pattern"></div>
      <div class="brand-mark"></div>
      <div class="flourish flourish-top" role="img" aria-label="Gold scroll ornament"></div>
      <h1 class="brand-name">HIDE WARDEN</h1>
      <div class="flourish flourish-bottom" role="img" aria-label="Gold scroll ornament"></div>
      <p class="claim">Treat &amp; Prevent<br>Ingrown Hair +<br>Calms Razor Burn<br>After Shaving</p>
      <h2 class="product-name">Botanical Healing Milk</h2>
      <div class="spacer"></div>
      <p class="scent">Acai Berry + Goats Milk</p>
      <p class="volume">3.5 fl oz 103 ml</p>
    </div>
  </article>

  <article class="label">
    <div class="label-inner">
      <div class="leaf-field" role="img" aria-label="Dark botanical leaf pattern"></div>
      <div class="brand-mark"></div>
      <div class="flourish flourish-top" role="img" aria-label="Gold scroll ornament"></div>
      <h1 class="brand-name">HIDE WARDEN</h1>
      <div class="flourish flourish-bottom" role="img" aria-label="Gold scroll ornament"></div>
      <p class="claim">Maintain Groin<br>Freshness &amp; Dryness<br>While Reducing Skin<br>Irritation &amp; Chafing</p>
      <h2 class="product-name">Botanical Healing Milk</h2>
      <div class="spacer"></div>
      <p class="scent">Cranberry + Pomogrenate</p>
      <p class="volume">3.5 fl oz 103 ml</p>
    </div>
  </article>

  <article class="label">
    <div class="label-inner">
      <div class="leaf-field" role="img" aria-label="Dark botanical leaf pattern"></div>
      <div class="brand-mark"></div>
      <div class="flourish flourish-top" role="img" aria-label="Gold scroll ornament"></div>
      <h1 class="brand-name">HIDE WARDEN</h1>
      <div class="flourish flourish-bottom" role="img" aria-label="Gold scroll ornament"></div>
      <p class="claim">Maintain Groin<br>Freshness &amp; Dryness<br>While Reducing Skin<br>Irritation &amp; Chafing</p>
      <h2 class="product-name">Manhood Freshner</h2>
      <div class="spacer"></div>
      <p class="scent">Organic Natural Healing</p>
      <p class="volume">3.5 fl oz 103 ml</p>
    </div>
  </article>

</main>
</body>
</html>
```